Design us a professional website for a Cannabis Staffing Agency

We already have a logo ready to go, but now we are looking for a few good web designs. We provide staffing for the Cannabis/Marijuana industry. We want a good balance of clean, simple and modern design but also embracing the exciting atmosphere of the Cannabis industry.

Here are examples of our competition, please note that most of these competitors design feel old and dated:

http://qrvworkforcecircle.example/
https://plorvik.example/plorvik-main-page
http://sapphirepathways.example/index.html
http://www.flaxcrew.example/medical-marijuana-staffing-recruiting
http://www.bramblestaffing.example/
www.takenupstaffing.example
www.pearfirst.example

I also would prefer an explanation of why you choose to design it the way you did? What was your thought process or did you use a template?

Requirements
Must have
• About Us Page
• Candidates Page
• Employer Page
• Job Opening Page
• Contact Us Page
Nice to have
• Colors to match the logo, good use of images and design to show the story. Our goal is to show our clients what we are about and not just tell them.

```html
<!DOCTYPE html>
<html lang="en">
<head>
<meta charset="utf-8">
<title>Greenrow — Cannabis Industry Staffing &amp; Recruiting</title>
<link rel="stylesheet" href="https://fonts.googleapis.com/css2?family=Open+Sans:ital,wght@0,300;0,400;0,600;0,700;1,400&display=swap">
<style>
  :root {
    --green: #5f9410;
    --green-dark: #4e7c0b;
    --ink: #2f2f2f;
    --text: #4a4a4a;
    --muted: #8a8a8a;
    --line: #e6e6e6;
    --topbar: #f4f4f4;
    --footer: #2a2a2a;
    --footer-text: #cfcfcf;
    --white: #ffffff;
  }
  * { box-sizing: border-box; margin: 0; padding: 0; }
  html, body { width: 705px; height: 1200px; overflow: hidden; }
  body { position: relative; font-family: "Open Sans", Arial, sans-serif; color: var(--text); background: var(--white); }
  a { color: inherit; text-decoration: none; }

  /* top bar */
  .topbar { position: absolute; left: 0; top: 0; width: 705px; height: 14px; background: var(--topbar); font-size: 5px; color: var(--ink); }
  .topbar .phone { position: absolute; left: 117px; top: 4px; }
  .topbar .auth { position: absolute; right: 118px; top: 4px; font-weight: 700; letter-spacing: .2px; }
  .topbar .auth .signup { color: var(--green); margin-left: 6px; }

  /* header */
  .site-header { position: absolute; left: 0; top: 14px; width: 705px; height: 40px; background: var(--white); }
  .brand { position: absolute; left: 117px; top: 10px; width: 90px; display: flex; align-items: center; gap: 3px; }
  .brand-mark { width: 22px; height: 22px; border-radius: 50%; background: var(--green); flex: none; }
  .brand-name { font-size: 10.5px; font-weight: 600; color: var(--green); letter-spacing: 0; white-space: nowrap; }
  .search { position: absolute; left: 213px; top: 14px; width: 110px; height: 14px; border-radius: 7px; background: var(--white); box-shadow: 0 1px 4px rgba(0,0,0,.15); font-size: 4.5px; color: #aaa; padding: 4.5px 0 0 6px; }
  .search svg { position: absolute; right: 6px; top: 3.5px; }
  .main-nav { position: absolute; left: 357px; top: 20px; width: 166px; display: flex; justify-content: space-between; font-size: 4.6px; color: var(--ink); font-weight: 400; white-space: nowrap; }
  .btn-seekers { position: absolute; left: 529px; top: 13px; width: 58px; height: 15px; border-radius: 8px; background: var(--green); color: var(--white); font-size: 4.8px; font-weight: 700; text-align: center; line-height: 15px; }

  /* hero */
  .hero { position: absolute; left: 0; top: 54px; width: 705px; height: 235px; overflow: hidden; }
  .hero-photo { position: absolute; inset: 0; background: linear-gradient(180deg, #8a8f94 0%, #6d6660 45%, #4e4540 100%); }
  .hero-shade { position: absolute; inset: 0; background: rgba(40,40,40,.35); }
  .hero-title { position: absolute; left: 0; top: 62px; width: 705px; text-align: center; color: var(--white); font-weight: 300; font-size: 28px; line-height: 31px; }
  .hero-sub { position: absolute; left: 0; top: 128px; width: 705px; text-align: center; color: #eee; font-size: 9.5px; font-weight: 300; }
  .hero-actions { position: absolute; left: 254px; top: 151px; display: flex; gap: 4px; }
  .btn { display: inline-block; border-radius: 11px; font-size: 5.5px; font-weight: 700; text-align: center; text-transform: uppercase; }
  .btn-primary { background: var(--green); color: var(--white); }
  .btn-outline { border: 1.5px solid var(--white); color: var(--white); }
  .hero-actions .btn { width: 91px; height: 21px; line-height: 20px; }

  /* quality staffing */
  .quality { position: absolute; left: 0; top: 289px; width: 705px; height: 241px; }
  .quality h2 { position: absolute; left: 117px; top: 38px; font-size: 16px; font-weight: 300; color: var(--ink); }
  .quality-copy { position: absolute; left: 117px; top: 69px; width: 210px; font-size: 6.8px; line-height: 14px; color: var(--text); }
  .quality .btn { position: absolute; left: 117px; top: 181px; width: 181px; height: 21px; line-height: 21px; }
  .feature-card { position: absolute; width: 142px; height: 46px; background: var(--white); box-shadow: 0 1px 7px rgba(0,0,0,.12); }
  .feature-card svg { position: absolute; left: 5px; top: 10px; }
  .feature-card h3 { position: absolute; left: 37px; top: 13px; font-size: 4.8px; font-weight: 700; color: var(--green); text-transform: uppercase; }
  .feature-card .snippet { position: absolute; left: 37px; top: 21px; width: 90px; font-size: 4.8px; line-height: 6px; color: var(--ink); }

  /* services */
  .services { position: absolute; left: 0; top: 530px; width: 705px; height: 225px; overflow: hidden; }
  .services-photo { position: absolute; inset: 0; background: linear-gradient(100deg, #e4e2df 0%, #f0efed 40%, #ebe7e3 70%, #e7e5e2 100%); }
  .services-veil { position: absolute; inset: 0; background: rgba(255,255,255,.55); }
  .service { position: absolute; top: 46px; width: 220px; text-align: center; }
  .service h2 { font-size: 15.5px; font-weight: 300; color: var(--ink); margin-bottom: 6px; }
  .service p { font-size: 6.8px; line-height: 14px; color: var(--text); }
  .service-direct { left: 115px; }
  .service-temp { left: 370px; width: 212px; }
  .services .btn { position: absolute; left: 289px; top: 173px; width: 126px; height: 21px; line-height: 21px; }

  /* testimonial */
  .testimonial { position: absolute; left: 0; top: 755px; width: 705px; height: 221px; border-bottom: 1px solid var(--line); }
  .video { position: absolute; left: 117px; top: 34px; width: 252px; height: 159px; background: #000; }
  .video svg { position: absolute; left: 110px; top: 64px; }
  .quote-mark { position: absolute; left: 385px; top: 64px; }
  .quote-text { position: absolute; left: 389px; top: 106px; width: 200px; font-size: 6.8px; line-height: 14px; color: var(--ink); }
  .quote-cite { position: absolute; left: 389px; top: 151px; border-left: 1px solid #ccc; padding-left: 5px; font-size: 4.3px; line-height: 7px; font-style: italic; color: var(--muted); }

  /* clients */
  .clients { position: absolute; left: 0; top: 976px; width: 705px; height: 86px; }
  .clients h2 { position: absolute; left: 0; top: 23px; width: 705px; text-align: center; font-size: 6.3px; font-weight: 600; color: var(--ink); letter-spacing: .2px; }
  .client-row { position: absolute; left: 117px; top: 45px; width: 470px; display: flex; justify-content: space-between; align-items: center; }
  .client { display: flex; align-items: center; gap: 3px; font-size: 9px; font-weight: 400; color: #9a9a9a; }
  .client i { display: inline-block; width: 8px; height: 8px; background: #b5b5b5; }

  /* footer */
  .site-footer { position: absolute; left: 0; top: 1062px; width: 705px; height: 138px; background: var(--footer); color: var(--footer-text); }
  .footer-col { position: absolute; top: 17px; list-style: none; font-size: 4.6px; line-height: 11px; text-transform: uppercase; }
  .social { position: absolute; left: 536px; top: 14px; display: flex; gap: 2px; }
  .social span { width: 15px; height: 15px; border-radius: 50%; border: 1px solid var(--white); }
  .footer-rule { position: absolute; left: 117px; top: 108px; width: 470px; height: 1px; background: #444; }
  .copyright { position: absolute; left: 118px; top: 122px; font-size: 4.6px; }
  .legal { position: absolute; right: 118px; top: 122px; font-size: 4.6px; }
  .legal span { margin: 0 4px; }
</style>
</head>
<body>

<div class="topbar">
  <span class="phone">+10-5550-0142</span>
  <span class="auth"><a href="#">LOGIN</a><a class="signup" href="#">SIGNUP</a></span>
</div>

<header class="site-header">
  <a class="brand" href="#"><span class="brand-mark"></span><span class="brand-name">GREENROW</span></a>
  <div class="search">SEARCH HERE
    <svg width="7" height="7" viewBox="0 0 10 10"><circle cx="4" cy="4" r="3" fill="none" stroke="#999" stroke-width="1.2"/><line x1="6.3" y1="6.3" x2="9" y2="9" stroke="#999" stroke-width="1.2"/></svg>
  </div>
  <nav class="main-nav">
    <a href="#">ABOUT US</a><a href="#">CANDIDATES</a><a href="#">EMPLOYER</a><a href="#">JOB OPENING</a><a href="#">CONTACT US</a>
  </nav>
  <a class="btn-seekers" href="#">JOB SEEKERS</a>
</header>

<section class="hero">
  <div class="hero-photo" role="img" aria-label="Photo of an audience seated in a bright seminar room listening to a presenter"></div>
  <div class="hero-shade"></div>
  <h1 class="hero-title">Marijuana and Cannabis Industry<br>Staffing &amp; Recruiting</h1>
  <p class="hero-sub">We connect cannabis companies with employees, largest and leading recruiting resource</p>
  <div class="hero-actions">
    <a class="btn btn-primary" href="#">Get Hired</a>
    <a class="btn btn-outline" href="#">Hire Someone</a>
  </div>
</section>

<section class="quality">
  <h2>Quality Staffing</h2>
  <p class="quality-copy">We recruit staff at all levels, from entry-level to executive and management level to board members, and we help a wide range of businesses in the industry: marijuana dispensaries and stores, cultivation centers, ancillary businesses that serve the cannabis industry, and nonprofit organizations focused on drug policy. We'll use our network, developed with more than a decade in the industry, to find you the right candidate.</p>
  <a class="btn btn-primary" href="#">Tell us about the position you are looking to fill</a>

  <article class="feature-card" style="left:344px;top:43px;">
    <svg width="26" height="26" viewBox="0 0 26 26" fill="none" stroke="#555" stroke-width="1"><rect x="11" y="3" width="10" height="18" rx="1.5"/><line x1="11" y1="6" x2="21" y2="6" stroke="#5f9410"/><circle cx="8" cy="14" r="4.5"/><line x1="5" y1="17.5" x2="2" y2="21" stroke-width="1.6"/></svg>
    <h3>New Job Posting Available</h3>
    <div class="snippet">A great snippet that describes how you can find a job for your....</div>
  </article>
  <article class="feature-card" style="left:393px;top:100px;">
    <svg width="26" height="26" viewBox="0 0 26 26" fill="none" stroke="#555" stroke-width="1"><circle cx="14" cy="14" r="8"/><line x1="12" y1="3.5" x2="16" y2="3.5"/><line x1="14" y1="14" x2="18" y2="10" stroke="#5f9410"/><line x1="2" y1="12" x2="6" y2="12"/><line x1="3" y1="16" x2="6" y2="16"/></svg>
    <h3>Flexible Staffing Solutions</h3>
    <div class="snippet">A great snippet that describes how you can find a job for your....</div>
  </article>
  <article class="feature-card" style="left:446px;top:159px;">
    <svg width="26" height="26" viewBox="0 0 26 26" fill="none" stroke="#555" stroke-width="1"><rect x="3" y="12" width="5" height="10"/><path d="M8 13 L12 7 L13 3 Q16 3 15 8 L14 11 L21 11 Q23 12 22 14 L20 21 Q19 22 17 22 L8 21" /><line x1="15" y1="15" x2="21" y2="15" stroke="#5f9410"/></svg>
    <h3>See Your Progress</h3>
    <div class="snippet">A great snippet that describes how you can find a job for your....</div>
  </article>
</section>

<section class="services">
  <div class="services-photo" role="img" aria-label="Faded photo of colleagues talking together around a meeting table"></div>
  <div class="services-veil"></div>
  <div class="service service-direct">
    <h2>Direct Hire Placements</h2>
    <p>Designed for clients with long-term, permanent positions. Our team of recruiters will gain an understanding of you and the position you're looking for. From there, we source candidates, screen candidates, reference and background check candidates. We coordinate our top candidates to interview with you. This means out of the dozens of you only interview the best of the best.</p>
  </div>
  <div class="service service-temp">
    <h2>Temporary Employees</h2>
    <p>Designed for clients with project work, seasonal peaks, unpredictable workloads, and other limited-term needs. Our team of temporary labor will arrive ready to work hard. Through all assignments, the candidate is employed by Greenrow. All state and federal taxes, workers compensation and payroll taxes are handled by us.</p>
  </div>
  <a class="btn btn-primary" href="#">Get Started Now</a>
</section>

<section class="testimonial">
  <div class="video" role="img" aria-label="Embedded company video">
    <svg width="32" height="32" viewBox="0 0 32 32"><circle cx="16" cy="16" r="14" fill="none" stroke="#fff" stroke-width="1.5"/><path d="M13 10 L22 16 L13 22 Z" fill="#fff"/></svg>
  </div>
  <svg class="quote-mark" width="36" height="28" viewBox="0 0 36 28" fill="#d9d9d9"><path d="M2 26 Q0 10 10 2 L13 4 Q7 10 8 14 Q14 14 14 20 Q14 27 8 27 Q3 27 2 26 Z"/><path d="M21 26 Q19 10 29 2 L32 4 Q26 10 27 14 Q33 14 33 20 Q33 27 27 27 Q22 27 21 26 Z"/></svg>
  <p class="quote-text">A great quote either from one of your client or one of your coaches that clearly focuses on the Unique Selling Proposition of Trellio and mentions one of the other advantages</p>
  <div class="quote-cite">Dana Holloway<br>Norvale Software</div>
</section>

<section class="clients">
  <h2>TRUSTED BY THESE COMPANIES</h2>
  <div class="client-row">
    <span class="client"><i></i>Ardent</span>
    <span class="client"><i></i>Corvo Group</span>
    <span class="client">Helix Orbit</span>
    <span class="client">Meridian</span>
    <span class="client">Tavo</span>
    <span class="client">Bexley</span>
    <span class="client">Norsk</span>
  </div>
</section>

<footer class="site-footer">
  <ul class="footer-col" style="left:118px;">
    <li>Looking to hire?</li><li>Looking for a job?</li><li>Jobs</li><li>Media</li><li>Investors</li><li>Employee portal</li><li>Media</li><li>Members only</li>
  </ul>
  <ul class="footer-col" style="left:272px;">
    <li>Who we are</li><li>Press</li><li>Careers</li><li>Support team</li><li>News and media</li><li>Greenrow blog</li><li>Contact us</li>
  </ul>
  <ul class="footer-col" style="left:402px;">
    <li>Direct hire placements</li><li>Temporary employees</li>
  </ul>
  <div class="social" aria-label="Social links"><span></span><span></span><span></span></div>
  <div class="footer-rule"></div>
  <div class="copyright">Copyright © 2017 Greenrow</div>
  <div class="legal">Legal Mentions<span>|</span>Privacy Policy<span>|</span>Terms &amp; Conditions</div>
</footer>

</body>
</html>
```